4R Capital business cards for a tech VC

We're starting a new Venture Capital that is focusing on bringing the best start ups from Israel to NYC
We need a business cards template for this that gives the sense of an entrepreneurial look
I don't want any religious signs on this even thought it's Israel
I'm looking for a techi feeling but not too crazy
The card should probably be in the same light blue as the logo and the logo in white

Target Market(s)

Investors

Industry/Entity Type

Tech

Contact Information for Business Card

The card needs to look slick and entrepreneurship like
The VC is focused on NYC and Tel Aviv so could be great to show something on the back side that is like NYC skyline or something like that
You can see the logo attached

Colors
0455a3
3276b5
85acd3
cedeed
eaf1f7

Requirements
Must have
• A very cool looking business card that shows we're a cutting edge tech VC with a focus on bringing start ups from Tel Aviv and leveraging the NYC ecosystem
Nice to have
• NYC skyline can be cool , maybe something that is connected to Tel Aviv

```html
<!DOCTYPE html>
<html lang="en">
<head>
<meta charset="utf-8">
<title>4R Capital – Business Cards</title>
<link href="https://fonts.googleapis.com/css2?family=Lato:wght@400;700;900&display=swap" rel="stylesheet">
<style>
  :root {
    --brand-cyan: #1ba8d8;
    --brand-blue: #1a86c4;
    --brand-deep: #0f6fae;
    --ink-grey: #6f7478;
    --rule-blue: #85acd3;
    --card-white: #fbfbfb;
    --stage: #e6ebf0;
    --white: #ffffff;
  }
  * { box-sizing: border-box; margin: 0; padding: 0; }
  html, body {
    width: 1200px; height: 780px; overflow: hidden;
    background: var(--stage);
    font-family: "Lato", Arial, sans-serif;
  }
  .canvas { position: relative; width: 1200px; height: 780px; }

  .card {
    position: absolute;
    border-radius: 4px;
    box-shadow: 0 14px 30px rgba(20, 40, 60, 0.22);
    overflow: hidden;
  }

  /* Front: portrait, white */
  .card-front {
    left: 120px; top: 75px; width: 360px; height: 630px;
    background: var(--card-white);
    text-align: center;
  }
  .front-logo {
    margin-top: 70px;
    display: flex; align-items: center; justify-content: center; gap: 12px;
    color: var(--brand-cyan);
    font-weight: 900; font-size: 40px; letter-spacing: 3px; text-transform: uppercase;
  }
  .logo-square { width: 22px; height: 22px; background: var(--brand-cyan); }
  .person-name {
    margin-top: 62px;
    color: var(--brand-cyan); font-weight: 900; font-size: 24px; letter-spacing: 1px;
    text-transform: uppercase;
  }
  .person-title { margin-top: 2px; color: var(--ink-grey); font-size: 18px; }
  .divider { width: 270px; height: 1px; background: var(--rule-blue); margin: 22px auto 18px; }
  .contact-label { color: var(--brand-cyan); font-weight: 700; font-size: 14px; }
  .contact-value { color: var(--ink-grey); font-size: 19px; letter-spacing: 1px; margin-bottom: 12px; }

  .skyline {
    position: absolute; left: 0; right: 0; bottom: 0; height: 190px;
    background: linear-gradient(180deg, rgba(26,134,196,0) 0%, #3a97cc 38%, var(--brand-blue) 100%);
  }
  .front-web {
    position: absolute; left: 0; right: 0; bottom: 26px;
    color: var(--white); font-size: 19px; letter-spacing: 1.5px;
  }

  /* Back: landscape, blue */
  .card-back {
    left: 540px; top: 210px; width: 630px; height: 360px;
    background: radial-gradient(ellipse at 55% 40%, #1fb6de 0%, var(--brand-cyan) 40%, var(--brand-deep) 100%);
    display: flex; flex-direction: column; align-items: center; justify-content: center;
    color: var(--white);
  }
  .back-logo {
    display: flex; align-items: center; gap: 16px;
    font-weight: 900; font-size: 54px; letter-spacing: 4px; text-transform: uppercase;
  }
  .back-logo .logo-square { width: 30px; height: 30px; background: var(--white); }
  .back-web { margin-top: 26px; font-size: 18px; letter-spacing: 2px; }
</style>
</head>
<body>
<main class="canvas">
  <section class="card card-front">
    <div class="front-logo"><span class="logo-square"></span>4R Capital</div>
    <p class="person-name">Daniel Reed</p>
    <p class="person-title">Managing Partner</p>
    <div class="divider"></div>
    <p class="contact-label">Phone</p>
    <p class="contact-value">(01) 5550 1842</p>
    <p class="contact-label">E-mail</p>
    <p class="contact-value">hello@4rcapital.co</p>
    <div class="skyline" role="img" aria-label="Blue silhouette of the New York skyline with bridges and a harbour statue"></div>
    <p class="front-web">www.4rcapital.co</p>
  </section>

  <section class="card card-back">
    <div class="back-logo"><span class="logo-square"></span>4R Capital</div>
    <p class="back-web">www.4rcapital.co</p>
  </section>
</main>
</body>
</html>
```